Landing Page for Martial Arts School

We'd like our page to look very much like http://www.tallpinestudio.com/. I've attached our text and you can see how I've tried to make it similar to their site in placement.
We'd like to do a darker green instead of their blue shading, obviously our logo (the dragon image) instead of theirs, our student photo or a better image you may choose, and instead of a solid block of text under "Welcome . . ." we'd like the USA Badge to the right of the text. At the bottom of the page we'd like a big button with our phone number. I know this is a lot to take in, but we're so looking forward to seeing your designs!

These designs are looking good! I'm sending each of you a few suggested tweaks for now! Best of luck!

As we enter the final few days of competition, I'd like to give a final word of thanks to all of our designers. We have moved out of good and into excellent, and we thank you all. We've also updated the student image we'd like you to use. All of the remaining designers will need to update their photos with the new one, please. Also, if you've one of the final designs, I'll be sending you a final set of notes and then we will be selecting someone. We may push back the final selection until Monday, depending.

Reason: We're going to discuss the finalized versions of your designs on Monday and make our final selection. If for some reason, none of the designers have made our suggested tweaks, then we still have another day.

```html
<!DOCTYPE html>
<html lang="en">
<head>
<meta charset="utf-8">
<title>Iron Crane Kung Fu</title>
<link rel="stylesheet" href="https://fonts.googleapis.com/css2?family=Arimo:wght@400;700&family=Open+Sans:wght@400&display=swap">
<style>
:root{
  --green:#2a6e0c;
  --green-dark:#235d0a;
  --green-text:#2f7a14;
  --grey-band:#e4e4e4;
  --grey-section:#eeeeee;
  --ink:#111;
  --muted:#333;
  --button:#3d3d3d;
  --footer:#1e1e1e;
  --social:#1f4fa0;
}
*{margin:0;padding:0;box-sizing:border-box}
html,body{width:970px;height:1200px;overflow:hidden;background:#fff}
body{font-family:"Arimo",Arial,sans-serif;color:var(--ink)}
.page{position:relative;width:970px;height:1200px;overflow:hidden}
.abs{position:absolute}

.nav{left:0;top:92px;width:970px;height:37px;background:var(--green)}
.nav a{position:absolute;top:11px;color:#fff;font-size:12.5px;text-decoration:none;letter-spacing:.2px}
.nav .sep{position:absolute;top:0;width:1px;height:37px;background:#3f8a1f}

.logo{left:434px;top:14px;width:104px;height:104px;border-radius:50%;background:#fff;border:3px solid #111;
  display:flex;align-items:center;justify-content:center;text-align:center;font-size:12px;font-weight:700;line-height:1.2;color:#111}

.slider-band{left:0;top:194px;width:970px;height:254px;background:var(--grey-band)}
.slider-arrow{width:62px;height:62px;border-radius:50%;background:#fff;top:246px}
.slider-arrow svg{position:absolute;top:23px}
.slide{left:134px;top:145px;width:702px;height:268px;border-radius:5px;
  background:linear-gradient(90deg,#3a3030 0%,#5a4a3a 30%,#6b5a40 55%,#4a4030 80%,#8a6a48 100%)}
.slide-shadow{left:150px;top:414px;width:670px;height:10px;border-radius:50%;background:radial-gradient(ellipse at center,rgba(0,0,0,.18),rgba(0,0,0,0) 70%)}

.contact-band{left:0;top:448px;width:970px;height:97px;background:var(--green)}
.contact-card{left:323px;top:458px;width:344px;height:71px;border-radius:4px;background:linear-gradient(#fafafa,#dcdcdc)}
.contact-card.dark{top:1038px;left:324px;background:linear-gradient(#3a3a3a,#080808);border:1px solid #555}
.phone-icon{position:absolute;left:12px;top:17px}
.phone-number{position:absolute;left:51px;top:10px;font-family:"Open Sans",sans-serif;font-size:24px;color:#222;letter-spacing:.5px;white-space:nowrap}
.phone-mail{position:absolute;left:52px;top:40px;font-family:"Open Sans",sans-serif;font-size:14.5px;color:#444;white-space:nowrap}
.dark .phone-number{color:#fff}
.dark .phone-mail{color:#fff}
.card-divider{position:absolute;left:228px;top:8px;width:1px;height:55px;background:#bbb}
.dark .card-divider{background:#555}
.social-box{position:absolute;left:240px;top:8px;width:92px;height:55px;border-radius:6px;background:var(--social);border:2px solid #fff;
  color:#fff;font-size:16px;font-weight:700;display:flex;align-items:center;justify-content:center}
.share-box{position:absolute;left:236px;top:18px;width:97px;height:33px;border-radius:2px;background:#3b68b8;border:1px solid #6d91d6;
  color:#fff;font-size:14px;display:flex;align-items:center;justify-content:center;letter-spacing:.5px}

.welcome{left:100px;top:563px;width:770px;text-align:center}
.welcome h1{font-weight:400;font-size:22.6px;color:#222;margin-bottom:16px}
.welcome p{font-size:11.3px;line-height:17.8px;margin-bottom:17.8px;color:#111}

.classes{left:0;top:782px;width:970px;height:237px;background:var(--grey-section)}
.class{position:absolute;top:14px}
.class h2{font-weight:400;font-size:22.6px;color:var(--green-text);white-space:nowrap}
.class h2 span{font-size:16px}
.class .rule{margin-top:7px;width:203px;border-top:2px dotted #777;height:0}
.class p{margin-top:12px;font-size:11.3px;line-height:17.8px;color:var(--muted)}
.class .btn{display:inline-block;margin-top:14px;background:var(--button);color:#fff;font-size:11.5px;padding:6px 10px;border-radius:3px}

.bottom-band{left:0;top:1019px;width:970px;height:105px;background:linear-gradient(var(--green-dark),var(--green) 30%,var(--green))}
.footer{left:0;top:1128px;width:970px;height:72px;background:var(--footer)}
.footer-links{position:absolute;left:88px;top:18px;font-size:12.5px;color:#ccc;word-spacing:2px}
.footer-links b{font-weight:400;margin:0 14px}
.copyright{position:absolute;left:88px;top:42px;font-size:11px;color:#ccc}
.badge{position:absolute;top:11px;width:54px;height:54px;border-radius:50%;background:#ddd;border:3px solid #555}
</style>
</head>
<body>
<div class="page">

  <nav class="abs nav">
    <a style="left:118px">HOME</a>
    <span class="sep" style="left:183px"></span>
    <a style="left:214px">ABOUT&nbsp; US</a>
    <span class="sep" style="left:309px"></span>
    <a style="left:336px">OUR CLASSES</a>
    <a style="left:567px">OUR SERVICES</a>
    <span class="sep" style="left:690px"></span>
    <a style="left:715px">CONTACT US</a>
  </nav>

  <div class="abs logo">Iron<br>Crane</div>

  <div class="abs slider-band"></div>
  <div class="abs slider-arrow" style="left:106px">
    <svg style="left:13px" width="12" height="16" viewBox="0 0 12 16"><path d="M9 1 L2 8 L9 15" fill="none" stroke="#555" stroke-width="2"/></svg>
  </div>
  <div class="abs slider-arrow" style="left:834px">
    <svg style="left:37px" width="12" height="16" viewBox="0 0 12 16"><path d="M3 1 L10 8 L3 15" fill="none" stroke="#555" stroke-width="2"/></svg>
  </div>
  <div class="abs slide-shadow"></div>
  <div class="abs slide" role="img" aria-label="Photo collage of an instructor and young students in black uniforms with yellow belts"></div>

  <div class="abs contact-band"></div>
  <div class="abs contact-card">
    <svg class="phone-icon" width="32" height="36" viewBox="0 0 32 36"><path d="M7 2 L12 2 L14 10 L10 13 Q13 21 20 26 L24 22 L31 25 L30 31 Q26 35 20 33 Q6 26 3 10 Q3 4 7 2 Z" fill="#222"/></svg>
    <div class="phone-number">555 010-2468</div>
    <div class="phone-mail">info@ironcrane.com</div>
    <span class="card-divider"></span>
    <div class="social-box">Follow Us</div>
  </div>

  <section class="abs welcome">
    <h1>Welcome to Iron Crane Kung Fu.</h1>
    <p>Lorem Ipsum is simply dummy text of the printing and typesetting industry. Lorem Ipsum has been the industry's standard dummy text ever since the 1500s, when an unknown printer took a galley of type and scrambled it to make a type specimen book. It has survived not only five centuries, but also the leap into electronic typesetting, remaining essentially unchanged. It was popularised in the 1960s with the release of Letraset sheets containing Lorem Ipsum passages, and more recently with desktop publishing software like Aldus PageMaker including versions of Lorem Ipsum.</p>
    <p>It has survived not only five centuries, but also the leap into electronic typesetting, remaining essentially unchanged. It was popularised in the 1960s Ipsum has been the industry's standard dummy text ever since the 1500s, when an unknown printer took a galley.</p>
  </section>

  <section class="abs classes">
    <article class="class" style="left:99px;width:210px">
      <h2>Beginners <span>(ages 3-7)</span></h2>
      <div class="rule"></div>
      <p>It is a fun, energetic introduction to the art. Students begin to learn forms. This class accepts young students.</p>
      <span class="btn">Read More</span>
    </article>
    <article class="class" style="left:368px;width:240px;top:12px">
      <h2>Intermediate <span>(ages 6-15)</span></h2>
      <div class="rule"></div>
      <p>Children learn martial arts, respect, and self-defense in a safe environment. This class is based on experience level and accepts students with some experience in the art.</p>
      <span class="btn">Read More</span>
    </article>
    <article class="class" style="left:663px;width:240px">
      <h2>Advanced <span>(ages 8-14)</span></h2>
      <div class="rule"></div>
      <p>For students who have some experience past the basic level. We cover more advanced topics, higher-kicks and more sparring.&nbsp; We prep our students for the challenges of confrontation, bullying, and self-defense.</p>
      <span class="btn">Read More</span>
    </article>
  </section>

  <div class="abs bottom-band"></div>
  <div class="abs contact-card dark">
    <svg class="phone-icon" width="32" height="36" viewBox="0 0 32 36"><path d="M7 2 L12 2 L14 10 L10 13 Q13 21 20 26 L24 22 L31 25 L30 31 Q26 35 20 33 Q6 26 3 10 Q3 4 7 2 Z" fill="#fff"/></svg>
    <div class="phone-number">555 010-2468</div>
    <div class="phone-mail">info@ironcrane.com</div>
    <span class="card-divider"></span>
    <div class="share-box">SHARE</div>
  </div>

  <footer class="abs footer">
    <div class="footer-links">Home<b>|</b>About&nbsp; Us<b>|</b>Our Classes<b>|</b>Our Services<b>|</b>Contact Us</div>
    <div class="copyright">© 2014 Iron Crane Kung Fu , Inc. All Rights Reserved</div>
    <span class="badge" style="left:733px"></span>
    <span class="badge" style="left:820px"></span>
  </footer>

</div>
</body>
</html>
```